Business cards and Stationary | Lumora Music Events

Hello! We need business cards and stationery for a new small business in the music industry. "Lumora is a high-end music agency which provides an unparalleled level of talent and personalized service to the realm entertainment, corporate events, and luxury weddings. Here is where the classical meets the contemporary and we can bring your vision to life.Keeping a steady finger on the pulse of current trends and consistently raising the bar for industry standards, Lumora continues to rise to the forefront of the music industry, providing the utmost professional, high-end, elegant, and engaging entertainment in Australia and World-Wide."

Target Market(s)

Class A. high profile corporate business.

Industry/Entity Type

Entertainment

Contact Information for Business Card

Lumora Music Events

Clare Yoshinaga
Director | Violinist

Level 7, 41 Caddow Lane
Sydney, 2000

Website: www.lumoramusicevents-demo.net
Phone number: 0455 318 602
Email: clare@lumoramusicevents-demo.net

Font styles to use
Serif
Sans Serif
Script

Colors
feeeee
0355a3
f59296
ffffff

Requirements
Nice to have
• Clean and sophisticated would be perfect.
• If there is a way to include the Instagram without being tacky, that would be awesome
• @lumoramusicevents
• Our website and logo have the following fonts:
• The primary logo is inspired and based on a font called BillionScript but the B is completely hand drawn and the rest is customised a bit to work together cohesively
• Monserrat Light - Is the Music part of the logo and as headers in the site
• Open Sans 300 and 400 (Light or Regular) is used mostly as the body text in the site
• If you want to access the website:
• www.lumoramusicevents-demo.net
• username: client
• password: preview

```html
<!DOCTYPE html>
<html lang="en">
<head>
<meta charset="utf-8">
<title>Lumora Music Events — Stationery</title>
<link rel="stylesheet" href="https://fonts.googleapis.com/css2?family=Montserrat:wght@300;400&family=Open+Sans:wght@300;400;600&family=Arimo:wght@400;700&display=swap">
<style>
  :root {
    --backdrop: #2a2a2d;
    --paper: #e9eaeb;
    --ink: #5a5a5c;
    --ink-dark: #3a3a3c;
    --rose: #b9837f;
    --coral: #e58489;
    --bar-grey: #555557;
    --card-dark: #231e1f;
  }
  * { margin: 0; padding: 0; box-sizing: border-box; }
  html, body { width: 1200px; height: 1200px; overflow: hidden; }
  body { background: var(--backdrop); position: relative; font-family: "Arimo", Arial, sans-serif; }

  .letterhead {
    position: absolute; left: 110px; top: 119px; width: 680px; height: 962px;
    background: var(--paper); color: var(--ink);
    box-shadow: 0 10px 30px rgba(0,0,0,.45);
    overflow: hidden;
  }
  .brand-mark {
    position: absolute; text-align: center;
    font-family: "Montserrat", sans-serif; font-weight: 300; color: var(--rose);
    letter-spacing: .12em; white-space: nowrap;
  }
  .letterhead .brand-mark { left: 0; right: 0; top: 78px; font-size: 30px; }
  .letter-block { position: absolute; left: 72px; width: 548px; font-size: 11.4px; line-height: 16px; }
  .letter-date { top: 203px; }
  .letter-recipient { top: 235px; }
  .letter-recipient strong { font-weight: 700; }
  .letter-salutation { top: 331px; }
  .letter-body { top: 363px; }
  .letter-body p { margin-bottom: 16px; text-align: justify; hyphens: auto; -webkit-hyphens: auto; }
  .letter-closing { top: 667px; }
  .signature-area {
    position: absolute; left: 64px; top: 686px; width: 250px; height: 28px;
    background: linear-gradient(90deg, rgba(40,40,42,.12), rgba(40,40,42,.04));
    border-radius: 4px;
  }
  .letter-signoff { top: 720px; }
  .letter-signoff strong { font-weight: 700; }

  .letter-footer { position: absolute; top: 888px; left: 0; width: 680px; font-family: "Open Sans", sans-serif; font-size: 11.6px; line-height: 13.7px; color: var(--ink-dark); }
  .footer-address { position: absolute; right: 527px; top: 13.7px; text-align: right; white-space: nowrap; }
  .contact-list { position: absolute; left: 170px; top: 0; list-style: none; }
  .contact-list li { display: flex; align-items: center; gap: 8px; white-space: nowrap; }
  .contact-list svg { width: 8px; height: 8px; flex: none; }

  .edge-band { position: absolute; left: 0; bottom: 0; width: 100%; height: 8px; display: flex; }
  .edge-band .band-coral { width: 162px; background: var(--coral); }
  .edge-band .band-gap { width: 4px; background: var(--paper); }
  .edge-band .band-grey { flex: 1; background: var(--bar-grey); }

  .card { position: absolute; left: 863px; width: 288px; height: 164px; box-shadow: 0 8px 20px rgba(0,0,0,.5); overflow: hidden; }
  .card-front { top: 330px; background: var(--paper); }
  .card-front .brand-mark { left: 132px; right: 12px; top: 60px; font-size: 13px; }
  .card-person { position: absolute; right: 196px; top: 106px; text-align: right; font-family: "Open Sans", sans-serif; font-size: 6.4px; line-height: 8px; color: var(--ink-dark); white-space: nowrap; }
  .card-person .person-name { font-weight: 600; font-size: 8.5px; line-height: 10px; color: var(--coral); }
  .card-person .rule { display: inline-block; width: 6px; height: 1px; background: var(--coral); vertical-align: middle; }
  .card-contacts { position: absolute; left: 105px; top: 117px; list-style: none; font-family: "Open Sans", sans-serif; font-size: 6.4px; line-height: 8px; color: var(--ink-dark); }
  .card-contacts li { display: flex; align-items: center; gap: 5px; white-space: nowrap; }
  .card-contacts svg { width: 5px; height: 5px; flex: none; }
  .card-front .edge-band { height: 5px; }
  .card-front .edge-band .band-coral { width: 96px; }
  .card-front .edge-band .band-gap { width: 3px; }

  .card-back { top: 530px; background: var(--card-dark); }
  .card-back .brand-mark { left: 0; right: 0; top: 62px; font-size: 20px; }
  .card-web { position: absolute; left: 0; right: 0; top: 137px; text-align: center; font-family: "Open Sans", sans-serif; font-size: 6.6px; letter-spacing: .08em; color: #ddd; }
  .card-web span { color: var(--coral); font-weight: 600; }
</style>
</head>
<body>

<svg width="0" height="0" style="position:absolute">
  <defs>
    <symbol id="icon-phone" viewBox="0 0 10 10"><path d="M2 1l2 2-1 1.2c.6 1.2 1.6 2.2 2.8 2.8L7 6l2 2-1.2 1.2C4.5 9 1 5.5.8 2.2z" fill="#e58489"/></symbol>
    <symbol id="icon-mail" viewBox="0 0 10 10"><rect x=".8" y="2" width="8.4" height="6" fill="none" stroke="#e58489" stroke-width="1"/><path d="M.8 2L5 5.6 9.2 2" fill="none" stroke="#e58489" stroke-width="1"/></symbol>
    <symbol id="icon-globe" viewBox="0 0 10 10"><circle cx="5" cy="5" r="4.2" fill="none" stroke="#e58489"/><path d="M.8 5h8.4M5 .8c-2.4 2.6-2.4 5.8 0 8.4M5 .8c2.4 2.6 2.4 5.8 0 8.4" fill="none" stroke="#e58489" stroke-width=".8"/></symbol>
    <symbol id="icon-dot" viewBox="0 0 10 10"><circle cx="5" cy="5" r="4.5" fill="#e58489"/></symbol>
  </defs>
</svg>

<article class="letterhead">
  <div class="brand-mark">LUMORA MUSIC</div>

  <div class="letter-block letter-date">January 1, 2050</div>
  <div class="letter-block letter-recipient">
    <strong>Oliver Brandt</strong><br>Managing Director<br>Co.Street, Building/Suite<br>City/State, Zip Code
  </div>
  <div class="letter-block letter-salutation">Dear Henry Caldwell,</div>
  <div class="letter-block letter-body">
    <p>Lorem ipsum dolor sit amet, consectetuer adipiscing elit, sed diam nonummy nibh euismod tincidunt ut laoreet dolore magna aliquam erat volutpat. Ut wisi enim ad minim veniam, quis nostrud exerci tation ullamcorper suscipit lobortis nisl ut aliquip ex ea commodo consequat. Duis dolore te feugait nulla facilisi. Nam liber tempor cum soluta nobis eleifend option congue nihil imperdiet doming id quod mazim placerat facer possim assum. Lorem ipsum dolor sit amet, consectetuer adipiscing elit, sed diam nonummy nibh euismod tincidunt ut laoreet dolore magna aliquam erat volutpat. Ut wisi enim ad minim veniam, quis nostrud exerci tation ullamcorper suscipit lobortis nisl ut aliquip ex ea commodo consequat.</p>
    <p>Consectetuer adipiscing elit, sed diam nonummy nibh euismod tincidunt ut laoreet dolore magna aliquam erat volutpat. Ut wisi enim ad minim veniam, quis nostrud exerci tation ullamcorper suscipit lobortis nisl ut aliquip ex ea commodo consequat. Consectetuer adipiscing elit, sed diam nonummy nibh euismod tincidunt ut laoreet dolore magna aliquam erat volutpat. Ut wisi enim ad minim veniam, quis nostrud exerci tation ullamcorper suscipit lobortis nisl ut aliquip ex ea commodo consequat.</p>
    <p>Duis dolore te feugait nulla facilisi. Nam liber tempor cum soluta nobis eleifend option congue nihil imperdiet doming id quod mazim placerat facer possim assum.Duis dolore te feugait nulla facilisi. Nam liber tempor cum soluta nobis eleifend option congue nihil imperdiet doming id quod mazim placerat facer possim assum.</p>
  </div>
  <div class="letter-block letter-closing">Sincerely Yours,</div>
  <div class="signature-area" role="img" aria-label="Handwritten signature of Marcus Ellery"></div>
  <div class="letter-block letter-signoff"><strong>Authorized Managing Director</strong><br>Company Name Here</div>

  <footer class="letter-footer">
    <div class="footer-address">Lumora Music<br>Level 7, 41 Caddow Lane<br>Sydney, 2000</div>
    <ul class="contact-list">
      <li><svg><use href="#icon-phone"/></svg>0455 318 602</li>
      <li><svg><use href="#icon-mail"/></svg>contact@lumoramusicevents-demo.net</li>
      <li><svg><use href="#icon-globe"/></svg>www.lumoramusicevents-demo.net</li>
      <li><svg><use href="#icon-dot"/></svg>@lumoramusicevents</li>
    </ul>
  </footer>
  <div class="edge-band"><span class="band-coral"></span><span class="band-gap"></span><span class="band-grey"></span></div>
</article>

<section class="card card-front">
  <div class="brand-mark">LUMORA MUSIC</div>
  <div class="card-person">
    <div class="person-name">Daniel Ashcroft</div>
    Managing Director<br><span class="rule"></span><br>Level 7, 41 Caddow Lane<br>Sydney, 2000
  </div>
  <ul class="card-contacts">
    <li><svg><use href="#icon-phone"/></svg>0455 318 602</li>
    <li><svg><use href="#icon-mail"/></svg>contact@lumoramusicevents-demo.net</li>
    <li><svg><use href="#icon-globe"/></svg>www.lumoramusicevents-demo.net</li>
    <li><svg><use href="#icon-dot"/></svg>@lumoramusicevents</li>
  </ul>
  <div class="edge-band"><span class="band-coral"></span><span class="band-gap"></span><span class="band-grey"></span></div>
</section>

<section class="card card-back">
  <div class="brand-mark">LUMORA MUSIC</div>
  <div class="card-web">www.<span>lumoramusicevents-demo</span>.net</div>
</section>

</body>
</html>
```